Mossy Den Pet Supply

Thank you for your interest in this design contest. We are always welcome to questions and are looking forward to seeing what you can come up with.

We work on a Bootstrap platform with our custom built CMS. We require all designs to be sized accordingly with the bootstrap grid system found here: http://fernlattice.com/css/#grid

At the start of a competition, we are looking for general Home Page Design concepts and an example product grid page.

Homepage: Slide Show/Featured Products/Specials

example website as a reference:https://www.mintcollarworks.com/

Store Product Grid: Show a grid of product thumbnails. Included elements are thumbnail and price. Also included are filters (sort by, show by grid/list).

No photos at this time but Logo is attached. Looking for good quality photo's around the web. Please read the attached creative brief in depth to get an idea f what the client is looking for. Thanks!

```html
<!DOCTYPE html>
<html lang="en">
<head>
<meta charset="utf-8">
<title>Mossy Den Pet Supply</title>
<link href="https://fonts.googleapis.com/css2?family=Open+Sans:wght@400;600;700;800&display=swap" rel="stylesheet">
<style>
:root{
  --green:#8cc63f;
  --green-dark:#6fa52a;
  --ink:#333;
  --muted:#888;
  --line:#e2e2e2;
  --nav:#2a2a2a;
  --panel:#f4f4f4;
  --footer:#ededed;
  --bottom:#2f2f2f;
  --star:#f5a623;
  --price-old:#e8573c;
}
*{box-sizing:border-box;margin:0;padding:0}
html,body{width:1200px;height:2216px;overflow:hidden}
body{font-family:"Open Sans",Arial,sans-serif;color:var(--ink);background:#fff;font-size:13px}
.wrap{width:980px;margin:0 auto;position:relative}
a{color:inherit;text-decoration:none}

.topbar{height:24px;font-size:10px;color:var(--muted);border-bottom:1px solid var(--line)}
.topbar .wrap{display:flex;justify-content:space-between;align-items:center;height:24px}
.topbar nav span{margin-left:14px}

.header{height:128px}
.header .wrap{display:flex;align-items:center;height:128px;justify-content:space-between}
.brand{display:flex;align-items:center;gap:12px}
.brand-mark{width:44px;height:44px;background:var(--green)}
.brand-name{font-weight:800;font-size:24px;color:var(--ink);line-height:1.05;width:170px}
.search{width:340px;height:30px;border:1px solid #ccc;display:flex;align-items:center;justify-content:space-between;padding:0 10px;color:#aaa;font-size:11px;margin-left:60px}
.cart{width:190px;height:78px;background:var(--green);color:#fff;display:flex;align-items:center;gap:12px;padding:0 16px}
.cart-icon{width:34px;height:30px}
.cart b{display:block;font-size:17px}
.cart small{font-size:11px}

.mainnav{background:var(--nav);height:40px}
.mainnav ul{list-style:none;display:flex;height:40px}
.mainnav li{color:#fff;font-size:12px;font-weight:600;padding:0 20px;line-height:40px}
.mainnav li.active{background:var(--green)}

.hero{height:280px;position:relative;background:linear-gradient(100deg,#e8e4dc 0%,#d9d1c4 40%,#b9a68e 70%,#cfc6b8 100%)}
.hero-caption{position:absolute;left:40px;top:70px}
.hero-caption h1{background:var(--green);color:#fff;font-size:24px;font-weight:700;padding:8px 16px;display:inline-block}
.hero-caption p{background:rgba(0,0,0,.6);color:#fff;font-size:13px;padding:6px 16px;margin-top:4px;display:inline-block}

.features{display:flex;gap:24px;margin-top:48px}
.feature{flex:1;height:160px;border:1px solid var(--line);display:flex;position:relative}
.feature-icon{width:64px;background:var(--green);display:flex;justify-content:center;padding-top:20px}
.feature-body{padding:16px 18px;font-size:11px;color:var(--muted);line-height:1.6}
.feature-body h3{color:var(--ink);font-size:14px;margin-bottom:6px}
.feature-body .more{position:absolute;right:16px;bottom:12px;color:var(--green);font-weight:600}

.section-head{display:flex;align-items:center;border-bottom:1px solid var(--line);margin-top:40px;height:44px;font-size:10px;color:var(--muted)}
.section-head h2{font-size:19px;font-weight:600;color:var(--ink);margin-right:40px}
.select{border:1px solid #ccc;width:90px;height:22px;margin-left:8px;display:inline-block;vertical-align:middle}
.pager{margin-left:auto;display:flex;gap:6px;align-items:center}
.pager span.n{border:1px solid #ccc;padding:1px 5px}
.pager span.on{background:var(--green);color:#fff;border-color:var(--green)}

.products{display:flex;gap:24px;margin-top:20px}
.product{flex:1;border:1px solid var(--line);padding:10px}
.product .thumb{height:200px}
.t1{background:linear-gradient(160deg,#f3f3f3,#d8c6b4 55%,#8a5a3a)}
.t2{background:linear-gradient(160deg,#f3f3f3,#a0764e 60%,#5e3a22)}
.t3{background:linear-gradient(160deg,#f3f3f3,#d9cdb7 55%,#9b8a6f)}
.t4{background:linear-gradient(160deg,#f3f3f3,#9fcde6 40%,#f2a9c4 70%,#e9d36a)}
.product h4{text-align:center;font-size:13px;margin:12px 0 8px}
.product .row{display:flex;justify-content:space-between;align-items:center;font-size:11px;border-top:1px solid var(--line);padding-top:8px}
.old{color:var(--price-old);text-decoration:line-through}
.btn-cart{background:var(--green);color:#fff;font-size:9px;font-weight:700;padding:4px 8px}
.stars{color:var(--star);font-size:12px;letter-spacing:1px}

.promos{display:flex;gap:24px;margin-top:70px}
.promo{flex:1;height:160px;display:flex;align-items:center;justify-content:center;text-align:center;font-weight:800;font-size:20px;color:var(--green);border:4px solid var(--green);flex-direction:column;gap:8px}
.promo.support{border:1px solid var(--line);flex-direction:row;justify-content:flex-start;text-align:left;font-size:13px;color:var(--ink);padding:16px;gap:14px}
.agent{width:90px;height:120px;background:linear-gradient(180deg,#e9e2d8,#b9a894)}
.support h5{font-size:18px;font-weight:700}
.support p{font-size:11px;color:var(--muted);margin:4px 0 8px}
.chat{background:var(--green);color:#fff;padding:5px 14px;font-size:13px;display:inline-block}

.specials{margin-top:64px;border:1px solid var(--line)}
.tabs{display:flex;background:var(--panel);height:40px;border-bottom:1px solid var(--line);font-size:12px;font-weight:700}
.tabs span{padding:0 24px;line-height:40px}
.tabs span.on{background:#fff;border-bottom:2px solid var(--green)}
.special-grid{display:grid;grid-template-columns:repeat(3,1fr);gap:26px 20px;padding:26px 40px}
.special{display:flex;gap:14px;align-items:center}
.special .dot{width:64px;height:64px;border-radius:50%;background:radial-gradient(circle,#c89a6a,#7a4a2a);flex:none}
.special h6{font-size:12px}
.special p{font-size:10px;color:var(--muted)}
.view-all{text-align:right;padding:0 20px 16px;font-size:11px}

.footer{background:var(--footer);margin-top:60px;height:300px}
.footer .wrap{display:flex;gap:30px;padding-top:28px}
.col{flex:1;font-size:10px;color:#666;line-height:1.9}
.col h5{font-size:14px;color:var(--ink);font-weight:600;margin-bottom:10px}
.badge{width:80px;height:26px;background:#d7d7d7;margin-top:12px;display:inline-block}
.field{height:24px;background:#fff;border:1px solid #ccc;margin-bottom:6px}
.field.tall{height:60px}
.submit{background:var(--nav);color:#fff;padding:3px 12px;display:inline-block}
.bottombar{background:var(--bottom);height:40px;color:#bbb;font-size:10px}
.bottombar .wrap{display:flex;justify-content:space-between;align-items:center;height:40px}
.cards{display:flex;gap:6px}
.cards i{width:30px;height:18px;background:#fff;border-radius:2px;display:block}
</style>
</head>
<body>
<div class="topbar"><div class="wrap"><span>Call us free: 123 456 7890</span><nav><span>My account</span><span>Wishlist</span><span>My Cart</span><span>Check Out</span><span>Login</span></nav></div></div>

<header class="header"><div class="wrap">
  <div class="brand"><div class="brand-mark"></div><div class="brand-name">Mossy Den Pet Supply</div></div>
  <div class="search">Search...<svg width="12" height="12" viewBox="0 0 12 12"><circle cx="5" cy="5" r="4" fill="none" stroke="#999" stroke-width="1.5"/><line x1="8" y1="8" x2="11" y2="11" stroke="#999" stroke-width="1.5"/></svg></div>
  <div class="cart"><svg class="cart-icon" viewBox="0 0 34 30"><path d="M2 3h5l4 16h17l3-11H9" fill="none" stroke="#fff" stroke-width="2.5"/><circle cx="13" cy="25" r="2.5" fill="#fff"/><circle cx="26" cy="25" r="2.5" fill="#fff"/></svg><div><b>My Cart</b><small>0 items - $0.00</small></div></div>
</div></header>

<nav class="mainnav"><div class="wrap"><ul><li class="active">Home</li><li>Blog</li><li>Reservations</li><li>Event Calendar</li><li>Photo Gallery</li><li>Video Gallery</li><li>Locator</li><li>Contact Us</li></ul></div></nav>

<div class="wrap">
  <section class="hero" role="img" aria-label="Woman walking several small dogs on leashes along a city street">
    <div class="hero-caption"><h1>Welcome To Mossy Den Pet Supply</h1><br><p>Lorem Ipsum Dolor Sit Amet Consectetuer Adipiscing</p></div>
  </section>

  <section class="features">
    <div class="feature"><div class="feature-icon"><svg width="30" height="30" viewBox="0 0 30 30"><circle cx="15" cy="15" r="11" fill="none" stroke="#fff" stroke-width="3"/></svg></div><div class="feature-body"><h3>Dog Collars</h3>Lorem Ipsum Dolor<br>Lorem ipsum dolor sit amet, consectetuer adipiscing elit sed diam nonummy.<a class="more">Read More »</a></div></div>
    <div class="feature"><div class="feature-icon"><svg width="30" height="30" viewBox="0 0 30 30"><path d="M8 4v14a7 7 0 0 0 14 0" fill="none" stroke="#fff" stroke-width="3"/></svg></div><div class="feature-body"><h3>Dog Leashes</h3>Lorem Ipsum Dolor<br>Lorem ipsum dolor sit amet, consectetuer adipiscing elit sed diam nonummy.<a class="more">Read More »</a></div></div>
    <div class="feature"><div class="feature-icon"><svg width="30" height="30" viewBox="0 0 30 30"><rect x="3" y="10" width="24" height="12" rx="3" fill="none" stroke="#fff" stroke-width="3"/></svg></div><div class="feature-body"><h3>Dog Bed</h3>Lorem Ipsum Dolor<br>Lorem ipsum dolor sit amet, consectetuer adipiscing elit sed diam nonummy.<a class="more">Read More »</a></div></div>
  </section>

  <div class="section-head"><h2>New Products</h2>CATEGORY <span class="select"></span><div class="pager">PAGE <span class="n on">1</span><span class="n">2</span><span class="n">3</span><span class="n">4</span> &nbsp;‹ PREV &nbsp; NEXT ›</div></div>

  <section class="products">
    <div class="product"><div class="thumb t1" role="img" aria-label="Brown leather dog leashes"></div><h4>Dog Leashes</h4><div class="row"><b>$ 160.00</b><span class="old">$ 180.00</span></div><div class="row" style="border:0"><span class="btn-cart">ADD TO CART</span><span class="stars">★★★★★</span></div></div>
    <div class="product"><div class="thumb t2" role="img" aria-label="Leather dog collar"></div><h4>Dog Collars</h4><div class="row"><b>$ 160.00</b><span class="old">$ 180.00</span></div><div class="row" style="border:0"><span class="btn-cart">ADD TO CART</span><span class="stars">★★★★★</span></div></div>
    <div class="product"><div class="thumb t3" role="img" aria-label="Cushioned dog beds"></div><h4>Dog Beds</h4><div class="row"><b>$ 160.00</b><span class="old">$ 180.00</span></div><div class="row" style="border:0"><span class="btn-cart">ADD TO CART</span><span class="stars">★★★★★</span></div></div>
    <div class="product"><div class="thumb t4" role="img" aria-label="Colorful dog toys"></div><h4>Dog Toys</h4><div class="row"><b>$ 160.00</b><span class="old">$ 180.00</span></div><div class="row" style="border:0"><span class="btn-cart">ADD TO CART</span><span class="stars">★★★★★</span></div></div>
  </section>

  <section class="promos">
    <div class="promo"><svg width="50" height="44" viewBox="0 0 50 44"><path d="M25 42 5 22A11 11 0 0 1 25 8a11 11 0 0 1 20 14z" fill="var(--green)"/></svg>100% SATISFACTION<br>GUARANTEED</div>
    <div class="promo support"><div class="agent" role="img" aria-label="Support agent wearing a headset"></div><div><h5>LIVE SUPPORT</h5><p>Online Now Click below<br>button to start a chat</p><span class="chat">Chat Now</span></div></div>
    <div class="promo"><svg width="46" height="44" viewBox="0 0 46 44"><rect x="4" y="16" width="38" height="26" fill="var(--green)"/><rect x="2" y="10" width="42" height="8" fill="var(--green-dark)"/><rect x="20" y="10" width="6" height="32" fill="#fff"/></svg>GREAT DAILY DEALS<br>SHOP NOW!</div>
  </section>

  <section class="specials">
    <div class="tabs"><span class="on">Specials</span><span>Best Sellers</span></div>
    <div class="special-grid">
      <div class="special"><div class="dot" role="img" aria-label="Product thumbnail"></div><div><h6>Lorem Ipsum Dolor</h6><p>Lorem ipsum dolor sit amet adipiscing</p><span class="stars">★★★★★</span></div></div>
      <div class="special"><div class="dot" role="img" aria-label="Product thumbnail"></div><div><h6>Lorem Ipsum Dolor</h6><p>Lorem ipsum dolor sit amet adipiscing</p><span class="stars">★★★★★</span></div></div>
      <div class="special"><div class="dot" role="img" aria-label="Product thumbnail"></div><div><h6>Lorem Ipsum Dolor</h6><p>Lorem ipsum dolor sit amet adipiscing</p><span class="stars">★★★★★</span></div></div>
      <div class="special"><div class="dot" role="img" aria-label="Product thumbnail"></div><div><h6>Lorem Ipsum Dolor</h6><p>Lorem ipsum dolor sit amet adipiscing</p><span class="stars">★★★★★</span></div></div>
      <div class="special"><div class="dot" role="img" aria-label="Product thumbnail"></div><div><h6>Lorem Ipsum Dolor</h6><p>Lorem ipsum dolor sit amet adipiscing</p><span class="stars">★★★★★</span></div></div>
      <div class="special"><div class="dot" role="img" aria-label="Product thumbnail"></div><div><h6>Lorem Ipsum Dolor</h6><p>Lorem ipsum dolor sit amet adipiscing</p><span class="stars">★★★★★</span></div></div>
      <div class="special"><div class="dot" role="img" aria-label="Product thumbnail"></div><div><h6>Lorem Ipsum Dolor</h6><p>Lorem ipsum dolor sit amet adipiscing</p><span class="stars">★★★★★</span></div></div>
      <div class="special"><div class="dot" role="img" aria-label="Product thumbnail"></div><div><h6>Lorem Ipsum Dolor</h6><p>Lorem ipsum dolor sit amet adipiscing</p><span class="stars">★★★★★</span></div></div>
      <div class="special"><div class="dot" role="img" aria-label="Product thumbnail"></div><div><h6>Lorem Ipsum Dolor</h6><p>Lorem ipsum dolor sit amet adipiscing</p><span class="stars">★★★★★</span></div></div>
    </div>
    <div class="view-all">View All »</div>
  </section>
</div>

<footer class="footer"><div class="wrap">
  <div class="col"><h5>Contact Us</h5>Web: www.mossydenpets.com<br>Email: hello@mossydenpets.com<br>Phone: 123 456 7890<br>International: 987 654 321<br><span class="badge"></span> <span class="badge" style="width:50px"></span></div>
  <div class="col"><h5>Sitemap</h5>Home<br>Blog<br>Reservations<br>Event Calendar<br>Photo Gallery<br>Video Gallery<br>Locator<br>Contact Us</div>
  <div class="col"><h5>Latest Tweets</h5>New treats arrived today, fresh picks for every pup in the den.<br>2 hours ago<br>Weekend sale on beds and collars starts now, stop by soon.<br>1 day ago</div>
  <div class="col"><h5>Customer Feedback</h5><div class="field"></div><div class="field"></div><div class="field tall"></div><span class="submit">Submit</span></div>
</div></footer>
<div class="bottombar"><div class="wrap"><span>© 2014 Mossy Den Pet Supply. All Rights Reserved</span><div class="cards"><i></i><i></i><i></i><i></i></div></div></div>
</body>
</html>
```